Flyer für einen ambulanten Pflegedienst
Zielgruppe
Wir sind ein ambulanter Pflegedienst und suchen ansprechende Designs und Vorlagen für unsere Flyer. Die Zielgruppe sind pflegebedürftige ältere Menschen und deren Angehörigen. Die Flyer sollen in Briefkästen, bei Ärzten, Krankenhäusern, Physiotherapiepraxen etc. verteilt werden.
Aufgabenstellung
Ich bin offen für Vorschläge und habe keine bestimmten Vorstellungen.

```html
<!DOCTYPE html>
<html lang="de">
<head>
<meta charset="utf-8">
<title>Pflegedienst Lindenhof – Flyer</title>
<link rel="stylesheet" href="https://fonts.googleapis.com/css2?family=Fira+Sans:ital,wght@0,300;0,400;0,600;0,700;1,400&family=Allura&display=swap">
<style>
  :root {
    --green: #0f8a5a;
    --green-light: #8cc48f;
    --ink: #2b2b2b;
    --grey-text: #4a4a4a;
    --bokeh: #eef0ee;
    --page: #ffffff;
    --paper: #ffffff;
  }
  * { box-sizing: border-box; margin: 0; padding: 0; }
  html, body { width: 848px; height: 1200px; overflow: hidden; background: var(--page); }
  body { position: relative; font-family: "Fira Sans", sans-serif; color: var(--ink); }

  .flyer { position: absolute; top: 150px; width: 370px; height: 740px; background: var(--paper); overflow: hidden; outline: 1px solid #e6e8e6; }
  .flyer--front { left: 38px; }
  .flyer--back { left: 440px; }

  .bokeh { position: absolute; border-radius: 50%; background: var(--bokeh); }

  /* Front */
  .front-hero { position: absolute; left: 0; top: 0; width: 370px; height: 200px;
    background: radial-gradient(circle at 48% 35%, #9bbf6a 0, #6f9a4c 18%, #c9d3bf 38%, #e9ece6 62%, #ffffff 100%); }
  .front-hero::after { content: ""; position: absolute; inset: 0; background: linear-gradient(to bottom, rgba(255,255,255,0) 50%, #fff 100%); }
  .tagline { position: absolute; left: 0; right: 0; top: 168px; text-align: center; font-weight: 300; font-size: 17px; color: var(--grey-text); padding-left: 40px; letter-spacing: .3px; }
  .brand { position: absolute; left: 28px; top: 218px; display: flex; align-items: center; gap: 12px; }
  .brand-dot { width: 40px; height: 40px; border-radius: 50%; background: var(--green); flex: none; }
  .brand-name { font-weight: 700; font-size: 27px; line-height: 1.05; color: var(--ink); }
  .front-lead { position: absolute; left: 108px; top: 305px; font-size: 13px; color: var(--ink); letter-spacing: .3px; }
  .front-values { position: absolute; left: 108px; top: 330px; list-style: none; color: var(--green); font-size: 15px; line-height: 23px; }
  .front-web { position: absolute; left: 108px; top: 430px; font-weight: 600; font-size: 14.5px; color: var(--ink); }
  .front-photo { position: absolute; left: 0; top: 500px; width: 370px; height: 240px;
    background: linear-gradient(to bottom, #ffffff 0%, #eceee9 25%, #d8d4c8 60%, #c4bcae 100%); }

  /* Back */
  .services { position: absolute; right: 140px; top: 34px; list-style: none; text-align: right; font-size: 11px; line-height: 17px; color: var(--ink); }
  .back-photo-top { position: absolute; left: 236px; top: 22px; width: 134px; height: 248px;
    background: linear-gradient(160deg, #d9dde0 0%, #9ab0c4 35%, #a88a6e 70%, #7a6a58 100%); }
  .back-brand { position: absolute; left: 24px; top: 100px; font-size: 12px; font-weight: 600; color: var(--green); }
  .goal { position: absolute; left: 22px; top: 132px; font-weight: 300; font-size: 17px; line-height: 23px; color: var(--ink); }
  .intro { position: absolute; left: 22px; top: 282px; width: 320px; font-size: 10px; line-height: 16px; color: var(--ink); }
  .back-photo-hands { position: absolute; left: 0; top: 388px; width: 168px; height: 122px;
    background: linear-gradient(120deg, #c9b9a4 0%, #b7c7a0 50%, #8fae5a 100%); }
  .contact-note { position: absolute; left: 180px; top: 392px; width: 178px; font-style: italic; font-size: 10.5px; line-height: 14px; color: var(--ink); }
  .phone { display: flex; align-items: center; gap: 6px; margin: 5px 0 7px; font-style: normal; font-weight: 600; font-size: 13px; color: var(--green); }
  .phone svg { flex: none; }
  .back-scene { position: absolute; left: 0; top: 540px; width: 370px; height: 200px;
    background: linear-gradient(to bottom, #ffffff 0%, #eef0ee 35%, #e2e2dc 100%); }
  .script-tagline { position: absolute; left: 22px; top: 566px; font-family: "Allura", cursive; font-size: 34px; color: var(--green); }
  .footer-band { position: absolute; left: 0; top: 636px; width: 370px; height: 78px; background: rgba(255,255,255,.72); }
  .footer-address { position: absolute; left: 22px; top: 646px; font-size: 9.5px; line-height: 13px; }
  .footer-address strong { color: var(--green); font-weight: 600; }
  .footer-contact { position: absolute; left: 186px; top: 660px; font-size: 9.5px; line-height: 13px; }
</style>
</head>
<body>

<section class="flyer flyer--front">
  <div class="front-hero" role="img" aria-label="Foto: Hände halten ein herzförmiges grünes Baumgebilde im Sonnenlicht"></div>
  <span class="bokeh" style="left:258px;top:12px;width:78px;height:78px;background:rgba(255,255,255,.45)"></span>
  <p class="tagline">Ihr Wohl an erster Stelle</p>

  <span class="bokeh" style="left:250px;top:296px;width:76px;height:76px"></span>
  <span class="bokeh" style="left:292px;top:356px;width:110px;height:160px"></span>
  <span class="bokeh" style="left:138px;top:406px;width:76px;height:76px"></span>
  <span class="bokeh" style="left:196px;top:460px;width:150px;height:150px"></span>

  <div class="brand">
    <span class="brand-dot"></span>
    <span class="brand-name">Pflegedienst<br>Lindenhof</span>
  </div>
  <p class="front-lead">Ambulante Pflege im Raum Frankfurt</p>
  <ul class="front-values">
    <li>verlässlich</li>
    <li>individuell</li>
    <li>professionell</li>
  </ul>
  <p class="front-web">pflegedienst-lindenhof.de</p>
  <div class="front-photo" role="img" aria-label="Foto: ältere Frau im Rollstuhl im Gespräch mit einer Pflegerin in hellem Wohnraum"></div>
</section>

<section class="flyer flyer--back">
  <ul class="services">
    <li>Grundpflege</li>
    <li>häusliche Betreuung</li>
    <li>hauswirtschaftliche Hilfe</li>
    <li>Pflegeberatung</li>
  </ul>
  <div class="back-photo-top" role="img" aria-label="Foto: Pflegerin legt einer lächelnden Seniorin im Rollstuhl die Hände auf die Schultern"></div>
  <p class="back-brand">Pflegedienst Lindenhof</p>
  <h2 class="goal">Unser Ziel ist es,<br>Sie dabei zu unterstützen,<br>so lange wie möglich<br>selbstständig und sicher<br>in Ihrem Zuhause zu leben.</h2>

  <span class="bokeh" style="left:40px;top:262px;width:54px;height:54px"></span>
  <span class="bokeh" style="left:150px;top:330px;width:60px;height:60px"></span>
  <p class="intro">Mit Respekt, Professionalität und Einfühlungsvermögen begleiten wir unsere Patienten zuverlässig in jeder Lebensphase – von der Unterstützung im Alltag bis zur einfühlsamen Begleitung in schwierigen Momenten. Wir bieten Ihnen individuelle Pflege und Betreuung in Ihrer gewohnten Häuslichkeit.</p>

  <div class="back-photo-hands" role="img" aria-label="Foto: zwei Hände halten sich tröstend vor grünem Rasen"></div>
  <div class="contact-note">
    <p>Alle Leistungen finden Sie online auf unserer Webseite oder sie vereinbaren einen Termin mit uns.</p>
    <p class="phone">
      <svg width="15" height="15" viewBox="0 0 16 16" aria-hidden="true"><circle cx="8" cy="8" r="8" fill="#555"/><path d="M5.2 4.2l1.3-.3.8 1.9-.9.7c.5 1 1.2 1.8 2.2 2.3l.7-.9 1.9.8-.3 1.3c-.1.4-.5.6-.9.6C7.3 10.4 5.6 8.7 4.6 5.1c0-.4.2-.8.6-.9z" fill="#fff"/></svg>
      069 58120947
    </p>
    <p>Unsere Beratung ist kostenlos und unverbindlich. Auf Wunsch kommen wir auch zu Ihnen nach Hause, um in Ihrer gewohnten Umgebung alle Fragen zu klären.</p>
  </div>

  <div class="back-scene" role="img" aria-label="Foto, stark aufgehellt: Pflegerin und Seniorin im Rollstuhl in einem Wohnzimmer"></div>
  <p class="script-tagline">Ihr Wohl an erster Stelle</p>
  <div class="footer-band"></div>
  <address class="footer-address" style="font-style:normal">
    <strong>Pflegedienst Lindenhof</strong><br>
    Kastanienweg 12<br>
    65931 Frankfurt am Main
  </address>
  <address class="footer-contact" style="font-style:normal">
    Telefon: +49 69 58120947<br>
    E-Mail: info@pflegedienst-lindenhof.de<br>
    Bürozeiten: 08:00 - 14:00 Uhr
  </address>
</section>

</body>
</html>
```